We need a design for a contracting company website based in KSA, something modern with the same color theme as the attached logo. including a page for people who want to submit their CV and try to apply for a job.Also to include the "about us, contact us, gallery, Divisions, Supplies, etc...". If possible to have an interactive or moving background. Please disregard the "Keen Methods" Section in the attached profile.

Industry/Entity Type

Construction Company

Number of Pages Required

5+ page

Colors

Designer to choose colors to be used in the design.

Requirements
Must have
• Pages:
• about us, contact us, gallery, Divisions, Apply for a job, Supplies
Nice to have
• - Moving or interactive background

```html
<!DOCTYPE html>
<html lang="en">
<head>
<meta charset="utf-8">
<title>Cobaltrine Building Company</title>
<link rel="stylesheet" href="https://fonts.googleapis.com/css2?family=Ubuntu:wght@400;500;700&family=Open+Sans:wght@400;600;700&display=swap">
<style>
:root{
  --yellow:#f7b12c;
  --yellow-soft:#fbc85a;
  --cream:#fde8bb;
  --brown:#3b2f23;
  --brown-deep:#1e1713;
  --ink:#2f2418;
  --body:#5b4b3b;
  --black:#0b0b0b;
  --grey-band:#e7e5e2;
}
*{box-sizing:border-box;margin:0;padding:0}
html,body{width:1200px;height:4261px;overflow:hidden}
body{position:relative;background:#fff;font-family:"Open Sans",sans-serif;color:var(--body)}
.abs{position:absolute}
a{color:inherit;text-decoration:none}

/* top bar */
.topbar{left:0;top:0;width:1200px;height:41px;background:var(--black);color:#fff;font-size:10px}
.topbar .contact{left:222px;top:13px;display:flex;gap:22px}
.topbar .social{left:884px;top:13px;display:flex;gap:28px}
.topbar .social span{width:14px;height:14px;border-radius:50%;border:2px solid var(--yellow)}
.topbar .social span+span{border-color:#fff}

/* nav */
.nav{left:0;top:41px;width:1200px;height:67px;background:var(--brown)}
.nav .brand-plate{left:0;top:0;width:392px;height:67px;background:#fff;clip-path:polygon(0 0,370px 0,392px 33px,370px 67px,0 67px)}
.brand{display:flex;align-items:center;gap:8px;font-family:"Ubuntu",sans-serif;font-weight:500;color:var(--ink)}
.nav .brand{left:222px;top:23px;font-size:16px}
.brand .mark{width:18px;height:18px;background:var(--yellow)}
.nav .menu{left:408px;top:24px;display:flex;gap:21px;font-size:13px;color:#fff}
.nav .menu .active{color:var(--yellow);border-bottom:2px solid var(--yellow);padding-bottom:4px}
.nav .search{left:940px;top:0;width:40px;height:67px;background:var(--yellow);display:flex;align-items:center;justify-content:center}

/* hero */
.hero{left:0;top:108px;width:1200px;height:508px;overflow:hidden}
.hero .photo{inset:0;background:linear-gradient(100deg,#6f6a5e 0%,#8a8f6a 22%,#5d5a55 45%,#7b746d 70%,#8d8a85 100%)}
.hero .shade{inset:0;background:rgba(20,16,12,.35)}
.hero h1{left:467px;top:128px;font-family:"Ubuntu",sans-serif;font-weight:700;font-size:46px;line-height:55px;color:#fff;letter-spacing:1px}
.hero h1 em{font-style:normal;color:var(--yellow)}
.hero p{left:469px;top:248px;width:520px;font-size:17px;line-height:27px;color:#fff}
.hero .btn{left:469px;top:324px;width:116px;height:28px;border:2px solid var(--yellow);color:#fff;font-size:13px;font-weight:600;display:flex;align-items:center;justify-content:center;gap:8px}
.hero .btn b{color:var(--yellow)}
.hero .dots{left:566px;top:458px;display:flex;gap:6px;align-items:center}
.dots i{display:block;width:11px;height:11px;border-radius:50%;background:#fff}
.dots i.on{width:34px;border-radius:6px;background:var(--yellow)}

/* section titles */
.title{display:flex;align-items:center;gap:14px;font-family:"Ubuntu",sans-serif;font-weight:700;font-size:48px;color:var(--ink)}
.title .mark{width:40px;height:40px;background:var(--yellow)}
.lead{left:220px;width:760px;font-size:13.5px;line-height:19px;color:var(--body)}

/* about */
.about-blocks{left:0;top:894px;width:626px;height:377px;background:var(--yellow)}
.about-photo{left:222px;top:765px;width:376px;height:478px;background:linear-gradient(160deg,#b9a887 0%,#6d6152 40%,#2f2b28 100%)}
.about-text{left:631px;top:792px;width:350px}
.about-text h3{font-size:25px;line-height:35px;font-weight:700;color:var(--ink);margin-bottom:12px}
.about-text p{font-size:12px;line-height:22.6px;text-align:justify;margin-left:5px}
.about-text p+p{margin-top:8px;margin-left:10px}
.pill{height:26px;border-radius:13px;background:var(--yellow);color:#fff;font-size:13px;font-weight:600;display:flex;align-items:center;justify-content:center}

/* supplies */
.card{top:1543px;width:228px;height:254px;background:#fff;box-shadow:0 3px 6px rgba(0,0,0,.12);font-size:10.6px;line-height:15.6px;text-align:justify}
.card.hot{background:var(--yellow);color:#fff;box-shadow:0 4px 10px rgba(0,0,0,.25)}
.card .txt{position:absolute;left:22px;top:86px;width:184px}
.card .more{position:absolute;left:22px;top:210px;font-size:12px;font-weight:600;text-decoration:underline;color:var(--ink);display:flex;gap:6px;align-items:center}
.card.hot .more{color:#fff}
.gear{top:1498px;width:108px;height:108px;border-radius:50%;background:#fff;border:3px solid var(--yellow);display:flex;align-items:center;justify-content:center}
.gear.hot{border:none;box-shadow:0 3px 8px rgba(0,0,0,.2)}
.pager{top:1826px;width:26px;height:26px;border:2px solid var(--yellow);display:flex;align-items:center;justify-content:center}

/* gallery */
.gallery-head{left:0;top:1920px;width:1200px;height:208px;background:var(--cream)}
.gallery-body{left:0;top:2128px;width:1200px;height:622px;background:var(--brown-deep)}
.gallery-foot{left:0;top:2750px;width:1200px;height:25px;background:var(--cream)}
.tile{width:228px;height:227px}
.tile .img{position:absolute;left:0;top:0;width:228px;height:195px}
.tile .cap{position:absolute;left:0;top:195px;width:228px;height:32px;background:var(--yellow);color:#fff;font-size:13px;font-weight:600;padding:8px 14px}
.tile .veil{position:absolute;left:0;top:0;width:228px;height:195px;background:rgba(255,255,255,.78);display:flex;align-items:center;justify-content:center;gap:6px;font-family:"Ubuntu",sans-serif;font-size:15px;font-weight:500;color:var(--ink);text-decoration:underline}

/* divisions */
.div-text{left:220px;top:2993px;width:360px;font-size:14px;line-height:27.3px;text-align:justify}
.ring{left:618px;top:3001px;width:380px;height:380px;border-radius:50%;background:#fde2a6;display:flex;align-items:center;justify-content:center}
.ring .mid{width:330px;height:330px;border-radius:50%;background:var(--yellow);display:flex;align-items:center;justify-content:center}
.ring .pic{width:290px;height:290px;border-radius:50%;background:radial-gradient(circle at 50% 40%,#56708c 0%,#2a3a4d 60%,#182330 100%)}

/* apply */
.apply-band{left:0;top:3509px;width:1200px;height:372px;background:var(--grey-band)}
.agent{left:0;top:3435px;width:282px;height:405px;background:linear-gradient(180deg,#3a2a22 0%,#c9a98f 45%,#f3efea 100%);border-radius:140px 140px 0 0}
.apply h2{left:300px;top:3552px;width:320px;text-align:center;font-family:"Ubuntu",sans-serif;font-weight:700;font-size:44px;color:var(--ink)}
.apply p{left:300px;top:3642px;width:320px;text-align:center;font-size:12px;line-height:21.5px}
.form{left:631px;top:3500px;width:354px;height:381px;background:var(--yellow-soft);clip-path:polygon(0 22px,50% 0,100% 22px,100% 100%,0 100%)}
.form h3{position:absolute;left:0;top:34px;width:354px;text-align:center;font-family:"Ubuntu",sans-serif;font-weight:500;font-size:25px;color:var(--ink)}
.field{position:absolute;left:10px;width:334px;height:30px;border:1px solid #8a6424;font-size:11px;color:#5a4223;padding:8px 10px}
.upload{position:absolute;left:48px;top:294px;display:flex;align-items:center;gap:10px;font-size:11px;color:var(--ink)}
.upload b{font-weight:600}
.upload .choose{background:var(--ink);color:#fff;padding:4px 12px;font-size:10px}
.upload small{font-size:10px}
.submit{position:absolute;left:120px;top:332px;width:105px;height:30px;border:2px solid var(--ink);font-size:13px;font-weight:700;color:var(--ink);display:flex;align-items:center;justify-content:center;gap:8px}
.sketch-right{left:985px;top:3509px;width:215px;height:372px;background:linear-gradient(180deg,#f2f2f2,#dcdcdc)}

/* footer */
.foot-left{left:0;top:3881px;width:516px;height:331px;background:linear-gradient(90deg,#ececec,#fbfbfb 50%)}
.foot-left .brand{position:absolute;left:220px;top:40px;font-size:22px}
.foot-left .brand .mark{width:26px;height:26px}
.foot-left p{position:absolute;left:220px;top:95px;width:270px;font-size:12px;line-height:18.5px;text-align:justify}
.subscribe{position:absolute;left:220px;top:269px;width:265px;height:32px;background:var(--brown-deep);color:#bbb;font-size:10px;padding:10px}
.subscribe .send{position:absolute;right:0;top:0;width:38px;height:32px;background:var(--yellow);display:flex;align-items:center;justify-content:center}
.foot-right{left:516px;top:3881px;width:684px;height:331px;background:var(--brown);color:#fff}
.foot-right h4{position:absolute;top:26px;font-family:"Ubuntu",sans-serif;font-weight:700;font-size:22px}
.foot-right h4::after{content:"";display:block;width:60px;height:2px;background:var(--yellow);margin-top:6px}
.links{position:absolute;left:30px;top:78px;list-style:none;font-size:12px;line-height:27.3px}
.links li::before{content:"";display:inline-block;width:7px;height:7px;border:2px solid var(--yellow);border-radius:50%;margin-right:6px;vertical-align:middle}
.links li.on{color:var(--yellow)}
.addr{position:absolute;left:191px;display:flex;gap:14px;font-size:11px;line-height:14px}
.addr b{font-weight:600;display:block}
.addr svg{flex:none}
.f-social{position:absolute;left:191px;top:240px;display:flex;gap:13px}
.f-social span{width:32px;height:32px;border-radius:50%;border:2px solid var(--yellow)}
.thumb{position:absolute;left:373px;width:91px;height:46px}
.copyright{left:0;top:4212px;width:1200px;height:49px;background:#17120e;color:#fff;font-size:11px;text-align:center;padding-top:17px}
</style>
</head>
<body>

<header>
  <div class="abs topbar">
    <div class="abs contact"><span>&#9990; Call Us: +123 4567 890</span><span>&#9993; E-Mail Us: support@cobaltrine.com</span></div>
    <div class="abs social"><span></span><span></span><span></span></div>
  </div>
  <nav class="abs nav">
    <div class="abs brand-plate"></div>
    <div class="abs brand"><span class="mark"></span>Cobaltrine Building Company</div>
    <div class="abs menu">
      <a class="active">Home</a><a>About us</a><a>Divisions</a><a>Apply for a job</a><a>Supplies</a><a>Gallery</a><a>Contact us</a>
    </div>
    <div class="abs search">
      <svg width="22" height="22" viewBox="0 0 22 22"><circle cx="9" cy="9" r="7" fill="none" stroke="#3b2f23" stroke-width="2"/><line x1="14" y1="14" x2="20" y2="20" stroke="#3b2f23" stroke-width="2.5"/></svg>
    </div>
  </nav>
</header>

<section class="abs hero">
  <div class="abs photo" role="img" aria-label="Construction worker in hard hat and safety vest holding plans at a building site"></div>
  <div class="abs shade"></div>
  <h1 class="abs">BUILD YOUR<br><em>DREAM WITH PASSION</em></h1>
  <p class="abs">Lorem ipsum dolor sit amet, consectetur adipiscing elit, sed do eiusmod tempor incididunt ut labore et dolore magna aliqua.</p>
  <a class="abs btn">More Details <b>&#187;</b></a>
  <svg class="abs" style="left:0;top:420px" width="1200" height="88" viewBox="0 0 1200 88"><path d="M0,30 Q600,120 1200,30 L1200,88 L0,88Z" fill="#fff"/></svg>
  <div class="abs dots"><i class="on"></i><i></i><i></i></div>
</section>

<section class="about">
  <h2 class="abs title" style="left:220px;top:676px"><span class="mark"></span>About Us</h2>
  <div class="abs about-blocks"></div>
  <div class="abs about-photo" role="img" aria-label="Engineer with tool bag beside a pickup truck near power lines at sunset"></div>
  <div class="abs about-text">
    <h3>Lorem ipsum dolor sit amet, consectetur adipiscing elit,</h3>
    <p>sed do eiusmod tempor incididunt ut labore et dolore magna aliqua. Ut enim ad minim veniam, quis nostrud exercitation ullamco laboris nisi ut aliquip ex ea commodo consequat. Duis aute irure dolor in reprehenderit in voluptate velit esse cillum dolore eu fugiat nulla pariatur. Excepteur sint occaecat cupidatat non proident, sunt in culpa qui officia deserunt mollit anim id est laborum.sed do eiusmod tempor incididunt ut labore et dolore magna aliqua.</p>
    <p>Ut enim ad minim veniam, quis nostrud exercitation ullamco laboris nisi ut aliquip ex ea commodo consequat. Duis aute irure dolor in reprehenderit in voluptate velit esse cillum dolore eu fugiat nulla pariatur.</p>
  </div>
  <a class="abs pill" style="left:880px;top:1167px;width:100px">View More &#187;</a>
</section>

<section class="supplies">
  <h2 class="abs title" style="left:220px;top:1343px"><span class="mark"></span>Supplies</h2>
  <p class="abs lead" style="top:1434px">Lorem ipsum dolor sit amet, consectetur adipiscing elit, sed do eiusmod tempor incididunt ut labore et dolore magna aliqua. Ut enim ad minim veniam, quis nostrud exercitation ullamco laboris nisi ut aliquip ex ea commodo consequat.</p>

  <div class="abs card" style="left:220px"><div class="txt">Lorem ipsum dolor sit amet, consectetur adipiscing elit, sed do eiusmod tempor incididunt ut labore et dolore magna aliqua.Lorem ipsum dolor sit amet, consectetur adipiscing elit, sed do eiusmod tempor incididunt ut labore et dolore magna aliqua.</div><a class="more">Read More &#10230;</a></div>
  <div class="abs card hot" style="left:485px"><div class="txt">Lorem ipsum dolor sit amet, consectetur adipiscing elit, sed do eiusmod tempor incididunt ut labore et dolore magna aliqua.Lorem ipsum dolor sit amet, consectetur adipiscing elit, sed do eiusmod tempor incididunt ut labore et dolore magna aliqua.</div><a class="more">Read More &#10230;</a></div>
  <div class="abs card" style="left:753px"><div class="txt">Lorem ipsum dolor sit amet, consectetur adipiscing elit, sed do eiusmod tempor incididunt ut labore et dolore magna aliqua.Lorem ipsum dolor sit amet, consectetur adipiscing elit, sed do eiusmod tempor incididunt ut labore et dolore magna aliqua.</div><a class="more">Read More &#10230;</a></div>

  <div class="abs gear" style="left:279px"><svg width="58" height="58" viewBox="0 0 58 58"><g fill="#c4c4c4"><circle cx="29" cy="29" r="19"/><rect x="24" y="3" width="10" height="52"/><rect x="3" y="24" width="52" height="10"/><rect x="24" y="3" width="10" height="52" transform="rotate(45 29 29)"/><rect x="24" y="3" width="10" height="52" transform="rotate(-45 29 29)"/></g><circle cx="29" cy="29" r="8" fill="#fff"/></svg></div>
  <div class="abs gear hot" style="left:545px"><svg width="58" height="58" viewBox="0 0 58 58"><g fill="#3b2f23"><circle cx="29" cy="29" r="19"/><rect x="24" y="3" width="10" height="52"/><rect x="3" y="24" width="52" height="10"/><rect x="24" y="3" width="10" height="52" transform="rotate(45 29 29)"/><rect x="24" y="3" width="10" height="52" transform="rotate(-45 29 29)"/></g><circle cx="29" cy="29" r="8" fill="#fff"/></svg></div>
  <div class="abs gear" style="left:812px"><svg width="58" height="58" viewBox="0 0 58 58"><g fill="#c4c4c4"><circle cx="29" cy="29" r="19"/><rect x="24" y="3" width="10" height="52"/><rect x="3" y="24" width="52" height="10"/><rect x="24" y="3" width="10" height="52" transform="rotate(45 29 29)"/><rect x="24" y="3" width="10" height="52" transform="rotate(-45 29 29)"/></g><circle cx="29" cy="29" r="8" fill="#fff"/></svg></div>

  <div class="abs pager" style="left:570px"><svg width="14" height="8"><line x1="0" y1="4" x2="14" y2="4" stroke="#f7b12c" stroke-width="2"/></svg></div>
  <div class="abs pager" style="left:603px;background:var(--yellow)"><svg width="14" height="8"><path d="M0 4H13M9 0L13 4L9 8" stroke="#fff" stroke-width="2" fill="none"/></svg></div>
</section>

<section class="gallery">
  <div class="abs gallery-head"></div>
  <h2 class="abs title" style="left:220px;top:1960px"><span class="mark"></span>Gallery</h2>
  <p class="abs lead" style="top:2051px">Lorem ipsum dolor sit amet, consectetur adipiscing elit, sed do eiusmod tempor incididunt ut labore et dolore magna aliqua. Ut enim ad minim veniam, quis nostrud exercitation ullamco laboris nisi ut aliquip ex ea commodo consequat.</p>
  <div class="abs gallery-body"></div>

  <div class="abs tile" style="left:222px;top:2170px"><div class="img" role="img" aria-label="Team reviewing documents beside a yellow hard hat" style="background:linear-gradient(135deg,#8c4d4d,#d9d3cc 55%,#e6c15a)"></div><div class="cap">Project Name</div></div>
  <div class="abs tile" style="left:486px;top:2170px"><div class="img" role="img" aria-label="Engineers inspecting scaffolding on site" style="background:linear-gradient(135deg,#b3b3ad,#e0ded8)"></div><div class="veil">View More &#10230;</div><div class="cap">Project Name</div></div>
  <div class="abs tile" style="left:751px;top:2170px"><div class="img" role="img" aria-label="Engineers in hard hats discussing plans outdoors" style="background:linear-gradient(135deg,#9fb0a0,#4b4d52 55%,#c98a3e)"></div><div class="cap">Project Name</div></div>
  <div class="abs tile" style="left:222px;top:2431px"><div class="img" role="img" aria-label="Colleagues meeting at a desk with rolled plans and a hard hat" style="background:linear-gradient(135deg,#9c8878,#d8d2cc 55%,#e0a43a)"></div><div class="cap">Project Name</div></div>
  <div class="abs tile" style="left:486px;top:2431px"><div class="img" role="img" aria-label="Hands working over architectural drawings and a tablet" style="background:linear-gradient(135deg,#dcdcdc,#9a9ea5 60%,#e2e2e2)"></div><div class="cap">Project Name</div></div>
  <div class="abs tile" style="left:751px;top:2431px"><div class="img" role="img" aria-label="Handshake over a table with blue and yellow hard hats" style="background:linear-gradient(135deg,#eef0f2,#b8c1c9 55%,#e8b940)"></div><div class="cap">Project Name</div></div>

  <div class="abs dots" style="left:575px;top:2684px"><i style="background:var(--yellow)"></i><i></i><i></i></div>
  <div class="abs gallery-foot"></div>
</section>

<section class="divisions">
  <h2 class="abs title" style="left:220px;top:2843px"><span class="mark"></span>Divisions</h2>
  <p class="abs lead" style="top:2934px">Lorem ipsum dolor sit amet, consectetur adipiscing elit, sed do eiusmod tempor incididunt ut labore et dolore magna aliqua. Ut enim ad minim veniam, quis nostrud exercitation ullamco laboris nisi ut aliquip ex ea commodo consequat.</p>
  <p class="abs div-text">Lorem ipsum dolor sit amet, consectetur adipiscing elit, sed do eiusmod tempor incididunt ut labore et dolore magna aliqua. Ut enim ad minim veniam, quis nostrud exercitation ullamco laboris nisi ut aliquip ex ea commodo consequat. Duis aute irure dolor in reprehenderit in voluptate velit esse cillum dolore eu fugiat nulla pariatur. Excepteur sint occaecat cupidatat non proident, sunt in culpa qui officia deserunt mollit anim id est laborum.orem ipsum dolor sit amet, consectetur adipiscing .</p>
  <a class="abs pill" style="left:220px;top:3282px;width:98px">View More &#187;</a>
  <div class="abs ring"><div class="mid"><div class="pic" role="img" aria-label="Two engineers in hard hats reviewing a tablet in a plant"></div></div></div>
</section>

<section class="apply">
  <div class="abs apply-band"></div>
  <div class="abs agent" role="img" aria-label="Support agent wearing a headset"></div>
  <div class="abs sketch-right" role="img" aria-label="Line sketch of a building"></div>
  <h2 class="abs">Apply For Job</h2>
  <p class="abs">Sed ut perspiciatis unde omnis iste natus error sit voluptatem accusantium doloremque laudantium, totam rem aperiam, eaque ipsa quae ab illo inventore veritatis et quasi architecto beatae vitae dicta sunt explicabo. Nemo enim ipsam voluptatem quia voluptas sit aspernatur aut odit aut fugit, sed quia consequuntur magni dolores eos qui ratione voluptatem sequi nesciunt.</p>
  <form class="abs form">
    <h3>GET IN TOUCH</h3>
    <div class="field" style="top:75px">Name:</div>
    <div class="field" style="top:115px">Phone:</div>
    <div class="field" style="top:155px">E-Mail:</div>
    <div class="field" style="top:195px">Designation:</div>
    <div class="field" style="top:235px">Address:</div>
    <div class="upload"><b>Upload your CV:</b><span class="choose">Choose File</span><small>No File Chosen</small></div>
    <div class="submit">SUBMIT <svg width="16" height="8"><path d="M0 4H15M11 0L15 4L11 8" stroke="#2f2418" stroke-width="2" fill="none"/></svg></div>
  </form>
</section>

<footer>
  <div class="abs foot-left">
    <div class="brand"><span class="mark"></span>Cobaltrine Building Company</div>
    <p>Lorem ipsum dolor sit amet, consectetur adipiscing elit, sed do eiusmod tempor incididunt ut labore et dolore magna aliqua. Ut enim ad minim veniam, quis nostrud exercitation ullamco laboris nisi ut aliquip ex ea commodo consequat. Duis aute irure dolor in reprehenderit in voluptate velit esse cillum dolore eu fugiat nulla pariatur.</p>
    <div class="subscribe">Enter Your Mail<span class="send"><svg width="16" height="16" viewBox="0 0 16 16"><path d="M1 7L15 1L10 15L8 9Z" fill="#fff"/></svg></span></div>
  </div>
  <div class="abs foot-right">
    <h4 style="left:30px">Quick Links</h4>
    <h4 style="left:191px">Address</h4>
    <h4 style="left:373px">Gallery</h4>
    <ul class="links">
      <li class="on">Home</li><li>About us</li><li>Divisions</li><li>Apply for a job</li><li>Supplies</li><li>Gallery</li><li>Contact us</li>
    </ul>
    <div class="addr" style="top:78px"><svg width="18" height="22" viewBox="0 0 18 22"><path d="M9 1C4.6 1 1 4.4 1 8.6 1 14 9 21 9 21S17 14 17 8.6C17 4.4 13.4 1 9 1Z" fill="none" stroke="#fff" stroke-width="2"/><circle cx="9" cy="8.5" r="3" fill="#fff"/></svg><div><b>Location:</b>Place Name</div></div>
    <div class="addr" style="top:132px"><svg width="18" height="18" viewBox="0 0 18 18"><path d="M4 1L7 5L5 7Q7 11 11 13L13 11L17 14L15 17Q8 17 4 12T1 4Z" fill="#fff"/></svg><div><b>Call Us:</b>+123 4567 890</div></div>
    <div class="addr" style="top:180px"><svg width="24" height="16" viewBox="0 0 24 16"><rect x="0" y="0" width="24" height="16" fill="#fff"/><path d="M0 0L12 9L24 0" fill="none" stroke="#3b2f23" stroke-width="2"/></svg><div><b>E-Mail Us:</b>support@cobaltrine.com</div></div>
    <div class="f-social"><span></span><span></span><span></span></div>
    <div class="thumb" style="top:78px;background:linear-gradient(135deg,#8c4d4d,#d9d3cc 55%,#e6c15a)" role="img" aria-label="Project photo"></div>
    <div class="thumb" style="top:132px;background:linear-gradient(135deg,#9fb0a0,#4b4d52 55%,#c98a3e)" role="img" aria-label="Project photo"></div>
    <div class="thumb" style="top:185px;background:linear-gradient(135deg,#dcdcdc,#9a9ea5 60%,#e2e2e2)" role="img" aria-label="Project photo"></div>
  </div>
  <div class="abs copyright">© 2019 All Rights Reserved by COBALTRINE BUILDING COMPANY.</div>
</footer>

</body>
</html>
```